Theatre Company needs poster for a Christmas show.

We need a poster for an annual Christmas musical show call "A Plum Hush". The style is Jazzy/Lounge Christmas songs. The poster should be a mid-centry modern, Gilt Row-style design. I have attached the past year's poster for reference. The poster should include "VelNOVA Professional Series presents A Plum Hush" the date "December 18th, 2015" our phone number "512-555-0148 ext 207" and our website "vel-nova.org". The poster should also include the logos of our title sponsors (attached).

Target Market(s)

Lakeway, Texas residents, Adults, 21+

Industry/Entity Type

It Company

Font styles to use
Sans Serif

Requirements
Must have
• VelNOVA logo
• Show title "A Plum Hush"
• Date: December 18th, 2015
• Phone number: 512-555-0148 ext 207
• Web site: vel-nova.org
• Sponsor logos at the bottom (attached)
• Mid-century modern, Gilt Row-style design
• Christmas/Winter colors
Nice to have
• Singer/piano/microphone imagery
• cocktail imagery

```html
<!DOCTYPE html>
<html lang="en">
<head>
<meta charset="utf-8">
<title>A Plum Hush — VelNOVA Professional Series</title>
<link rel="stylesheet" href="https://fonts.googleapis.com/css2?family=Lobster&family=Montserrat:wght@600;700;800&display=swap">
<style>
  :root {
    --red-deep: #a8121b;
    --red: #d22a1c;
    --orange: #ee6a1a;
    --amber: #f5a41d;
    --yellow: #ffd83a;
    --gold-light: #fff07a;
    --gold: #e7b51d;
    --gold-dark: #7a4a05;
    --ink: #6e0b10;
    --band: #ffffff;
    --band-ink: #222222;
    --sponsor-ink: #1f3d7a;
  }
  * { margin: 0; padding: 0; box-sizing: border-box; }
  html, body { width: 849px; height: 1200px; overflow: hidden; background: #ffffff; }
  .poster {
    position: relative;
    width: 849px;
    height: 1200px;
    overflow: hidden;
    font-family: "Montserrat", Arial, sans-serif;
    background:
      radial-gradient(ellipse 60% 45% at 95% 15%, var(--yellow) 0%, rgba(255,216,58,0) 70%),
      linear-gradient(100deg, var(--red-deep) 0%, var(--red) 30%, var(--orange) 62%, var(--amber) 100%);
  }
  .presenter {
    position: absolute;
    top: 26px;
    left: 0;
    width: 100%;
    text-align: center;
    font-weight: 800;
    font-size: 27px;
    letter-spacing: 0.5px;
    color: var(--ink);
    text-transform: uppercase;
  }
  .singer-art {
    position: absolute;
    left: 110px;
    top: 62px;
    width: 380px;
    height: 990px;
    border-radius: 48% 48% 6% 6% / 22% 22% 2% 2%;
    background: linear-gradient(180deg, rgba(250,205,170,0.55) 0%, rgba(190,30,30,0.75) 45%, rgba(120,10,20,0.8) 100%);
  }
  .title {
    position: absolute;
    left: 300px;
    top: 470px;
    width: 480px;
    transform: rotate(-12deg);
    transform-origin: left top;
    font-family: "Lobster", cursive;
    line-height: 0.85;
    color: var(--yellow);
    -webkit-text-stroke: 3px var(--gold-dark);
    text-shadow: 5px 6px 0 rgba(90,20,0,0.55);
  }
  .title .lead { display: block; font-size: 150px; }
  .title .lead small { font-size: 80px; }
  .title .tail { display: block; font-size: 190px; padding-left: 90px; }
  .date {
    position: absolute;
    left: 395px;
    top: 820px;
    transform: rotate(-9deg);
    transform-origin: left top;
    font-weight: 800;
    font-size: 38px;
    color: var(--yellow);
    -webkit-text-stroke: 1.5px var(--gold-dark);
    text-shadow: 3px 3px 0 rgba(90,20,0,0.5);
    white-space: nowrap;
  }
  .stars { position: absolute; inset: 0; pointer-events: none; }
  .cocktail-art {
    position: absolute;
    left: 600px;
    top: 880px;
    width: 120px;
    height: 150px;
    clip-path: polygon(0 0, 100% 0, 55% 55%, 55% 92%, 85% 100%, 15% 100%, 45% 92%, 45% 55%);
    background: linear-gradient(180deg, var(--gold-light) 0%, var(--gold) 100%);
  }
  .footer {
    position: absolute;
    left: 0;
    bottom: 0;
    width: 100%;
    height: 147px;
    background: var(--band);
    display: flex;
    align-items: center;
    padding: 0 30px;
    gap: 26px;
  }
  .sponsor {
    display: flex;
    align-items: center;
    gap: 8px;
    font-weight: 700;
    font-size: 22px;
    color: var(--sponsor-ink);
    white-space: nowrap;
  }
  .sponsor-mark { width: 14px; height: 14px; border-radius: 50%; background: var(--sponsor-ink); }
  .contact {
    margin-left: auto;
    text-align: right;
    font-weight: 700;
    color: var(--band-ink);
    line-height: 1.15;
  }
  .contact .phone { font-size: 30px; text-transform: uppercase; }
  .contact .web { font-size: 38px; }
</style>
</head>
<body>
<main class="poster">
  <p class="presenter">VelNOVA Professional Series Presents</p>

  <div class="singer-art" role="img" aria-label="Halftone portrait of a lounge singer in a red halter dress"></div>

  <svg class="stars" width="849" height="1200" viewBox="0 0 849 1200" aria-hidden="true">
    <g fill="#ffd83a" stroke="#7a4a05" stroke-width="1.5">
      <polygon points="735,420 741,437 759,437 745,448 750,466 735,455 720,466 725,448 711,437 729,437"/>
      <polygon points="390,760 395,774 410,774 398,783 402,798 390,789 378,798 382,783 370,774 385,774"/>
      <polygon points="660,835 665,849 680,849 668,858 672,873 660,864 648,873 652,858 640,849 655,849"/>
    </g>
  </svg>

  <h1 class="title"><span class="lead"><small>A</small> Plum</span><span class="tail">Hush</span></h1>
  <p class="date">DECEMBER 18th, 2015</p>

  <div class="cocktail-art" role="img" aria-label="Martini glass with an olive garnish"></div>

  <footer class="footer">
    <div class="sponsor"><span class="sponsor-mark"></span>StepWell</div>
    <div class="sponsor">Ardent</div>
    <div class="sponsor">Lumen Frame</div>
    <div class="contact">
      <div class="phone">512-555-0148 ext 207</div>
      <div class="web">vel-nova.org</div>
    </div>
  </footer>
</main>
</body>
</html>
```